" O escritório Brunoro Arquitetura desenvolve projetosarquitetônicos e interiores, além de acompanhamento e administraçãao de obras. Tem a frente de sua gestão a arquiteta Mariana Forteso, que prioriza o atendimento exclusivo e diferenciado a cada um dos clientes, estabelecendo assim uma relação de proximidade, confiança e fidelização. Todos os projetos são desenvolvidos de acordo com o perfil do cliente, buscando sempre soluções inovadoras, criativas e acessíveis, em muitos casos utilizando materiais e soluções alternativas ao convencional, marca do escritório. O espaço físico do escritório reflete essa proposta de inovação e criatividade, que permite a acessibilidade da arquitetura a qualquer pessoa, desmistificando o status de que a boa arquitetura é acessível somente àqueles que possuem um alto poder aquisitivo. Todo o processo de concepção e posterior execução dos trabalhos é realizada entre os profissionais envolvidos e os clientes com total transparência, sendo a política de trabalho do escritório focada na ética, honestidade e respeito ao cliente, não havendo portanto o recebimento de reservas técnicas ou comissões de lojistas e empresas terceiras, para indicação de produtos. Assim, trabalhamos com total liberdade na concepção e especificação de materiais e soluções nos projetos. O escritório também tem ligação forte com as escolas de arquitetura da cidade, sendo um local de estágio e constante aprendizado para estudantes, que adquirem experiência profissional junto aos membros do escritório. A linguagem dos projetos, que deve se refletir na identidade visual da marca, busca a simplicidade dos materiais e formas, aplicadas da forma correta, gerando resultados simples, porém sofisticados. Priorizamos o uso dos materiais naturais em todos os projetos, mas prioritariamente o uso da madeira natural. Trabalhamos sempre com muito respeito pela história dos lugares, procurando sempre que possível preservar características originais que dão identidade aos lugares. "

```html
<!DOCTYPE html>
<html lang="pt-BR">
<head>
<meta charset="utf-8">
<title>Envelope Saco — Brunoro Arquitetura</title>
<link rel="stylesheet" href="https://fonts.googleapis.com/css2?family=Oswald:wght@500&family=Montserrat:wght@300;400&display=swap">
<style>
  :root {
    --bg-center: #f2f2f2;
    --bg-edge: #b4b4b4;
    --flap: #5e5f61;
    --paper: #ffffff;
    --fold: #dedede;
    --ink: #6a6b6d;
    --label-band: #58595b;
    --label-text: #ffffff;
  }
  html, body {
    margin: 0;
    padding: 0;
    overflow: hidden;
  }
  .canvas {
    position: relative;
    width: 1200px;
    height: 1200px;
    overflow: hidden;
    background: radial-gradient(circle at 50% 50%, var(--bg-center) 0%, #dcdcdc 55%, var(--bg-edge) 100%);
    font-family: "Montserrat", sans-serif;
  }
  .sheet-title {
    position: absolute;
    left: 0;
    top: 0;
    width: 1200px;
    height: 120px;
  }
  .sheet-title__text {
    font-family: "Oswald", sans-serif;
    font-weight: 500;
    font-size: 26px;
    fill: var(--label-text);
  }
  .dieline {
    position: absolute;
    left: 0;
    top: 0;
    width: 1200px;
    height: 1200px;
  }
  .flap { fill: var(--flap); }
  .panel { fill: var(--paper); }
  .fold-line { stroke: var(--fold); stroke-width: 2; }
  .return-address {
    font-family: "Montserrat", sans-serif;
    font-weight: 400;
    font-size: 9px;
    fill: var(--ink);
  }
  .brand-name {
    font-family: "Montserrat", sans-serif;
    font-weight: 300;
    fill: var(--ink);
  }
  .brand-dot {
    fill: none;
    stroke: var(--ink);
    stroke-width: 2;
  }
</style>
</head>
<body>
<main class="canvas">

  <svg class="sheet-title" viewBox="0 0 1200 120" aria-label="Envelope saco">
    <polygon fill="var(--label-band)" points="0,66 72,66 60,106 0,106"/>
    <polygon fill="var(--label-band)" points="96,40 420,40 406,82 82,82"/>
    <polygon fill="var(--label-band)" points="396,22 432,22 432,46"/>
    <text class="sheet-title__text" x="148" y="72">ENVELOPE SACO</text>
  </svg>

  <svg class="dieline" viewBox="0 0 1200 1200">
    <!-- flaps -->
    <path class="flap flap--side" d="M128,172 L104,172 Q76,178 76,214 L76,1012 Q76,1050 104,1060 L128,1060 Z"/>
    <path class="flap flap--top" d="M126,182 L142,162 Q152,150 174,150 L598,150 Q618,150 624,166 L630,182 Z"/>
    <path class="flap flap--bottom" d="M130,1054 L626,1054 L616,1084 Q612,1092 598,1092 L162,1092 Q148,1092 142,1084 Z"/>

    <!-- back panel -->
    <rect class="panel panel--back" x="126" y="180" width="504" height="876"/>

    <!-- front panel -->
    <path class="panel panel--front" d="M630,300 C760,250 900,330 1124,268 L1124,1056 L630,1056 Z"/>
    <line class="fold-line" x1="630" y1="300" x2="630" y2="1056"/>

    <!-- return address on back panel -->
    <g class="return-address" text-anchor="middle">
      <text x="380" y="946">Rua das Palmeiras, 214</text>
      <text x="380" y="958">Jardim Aurora | CEP 13000-000</text>
      <text x="380" y="970">Campinas/SP</text>
      <text x="380" y="994">Telefones: (19) 3200-0000 | (19) 98800-0000</text>
      <text x="380" y="1006">contato@brunoro.arq.br | www.brunoro.arq.br</text>
    </g>

    <!-- brand on front panel -->
    <g class="brand" text-anchor="middle">
      <circle class="brand-dot" cx="912" cy="924" r="16"/>
      <text class="brand-name" x="912" y="978" font-size="24" letter-spacing="6">BRUNORO</text>
      <text class="brand-name" x="912" y="1000" font-size="10" letter-spacing="6">ARQUITETURA</text>
    </g>
  </svg>

</main>
</body>
</html>
```